Flyer design for webdesign company

create a flyer that can be printed or sent as an email. The flyer needs to be professional, modern and engaging.

Reason: opportunity for all designers to get their designs in.

Target Market(s)

business owners that do not have a website

Industry/Entity Type

It Company

Font styles to use
Sans Serif

```html
<!DOCTYPE html>
<html lang="en">
<head>
<meta charset="utf-8">
<title>Web Design Flyer – novasites</title>
<link href="https://fonts.googleapis.com/css2?family=Montserrat:wght@800;900&family=Open+Sans:wght@400;600;700&family=Roboto+Condensed:wght@700&display=swap" rel="stylesheet">
<style>
  :root {
    --navy: #1c2452;
    --red: #e5262b;
    --deep-red: #a8232a;
    --yellow-light: #fff27a;
    --yellow: #f6d21a;
    --amber: #e0a811;
    --teal-light: #3b6c70;
    --teal: #2a5258;
    --teal-dark: #1b3740;
    --white: #ffffff;
    --ink: #1a1a1a;
    --grey: #5a5a5a;
    --pink: #e0258f;
    --pink-dark: #c4137a;
    --blue: #1f7fd1;
  }
  * { margin: 0; padding: 0; box-sizing: border-box; }
  html, body { width: 848px; height: 1200px; overflow: hidden; background: var(--white); }
  .flyer { position: relative; width: 848px; height: 1200px; overflow: hidden; background: var(--white); font-family: "Open Sans", Arial, sans-serif; }

  .hero-backdrop { position: absolute; left: 0; top: 0; width: 848px; height: 420px;
    background: radial-gradient(ellipse at 30% 35%, var(--yellow-light) 0%, var(--yellow) 45%, var(--amber) 100%); }

  .feature-band { position: absolute; left: 0; top: 340px; width: 848px; height: 566px; }

  .team-photo { position: absolute; left: 340px; top: 400px; width: 508px; height: 506px;
    background: linear-gradient(160deg, rgba(255,255,255,0.10) 0%, rgba(230,230,235,0.22) 50%, rgba(30,50,70,0.25) 100%); }

  .headline { position: absolute; left: 0; width: 848px; text-align: center; font-family: "Montserrat", Arial, sans-serif; font-weight: 900; line-height: 1; }
  .headline--navy { color: var(--navy); }
  .headline--red { color: var(--red); }
  .headline-attract { top: 80px; font-size: 50px; letter-spacing: 1px; }
  .headline-customers { top: 128px; font-size: 56px; letter-spacing: 1px; }
  .headline-make { top: 224px; font-size: 50px; letter-spacing: 1px; }
  .headline-money { top: 272px; font-size: 100px; letter-spacing: 3px; }

  .benefits { position: absolute; left: 26px; top: 474px; width: 440px; list-style: none; }
  .benefit { position: relative; padding-left: 40px; color: var(--white); font-size: 17px; line-height: 19px; margin-bottom: 17px; text-shadow: 0 1px 2px rgba(0,0,0,0.35); }
  .benefit--strong { font-weight: 700; }
  .benefit--caps { font-weight: 700; text-transform: uppercase; }
  .tick { position: absolute; left: 2px; top: 0; width: 30px; height: 26px; }

  .slogan { position: absolute; left: 0; width: 848px; text-align: center; font-family: "Open Sans", Arial, sans-serif; }
  .slogan-stop { top: 940px; color: var(--deep-red); font-weight: 700; font-size: 36px; }
  .slogan-stop .slogan-big { font-size: 52px; }
  .slogan-sub { top: 1006px; color: var(--ink); font-size: 28px; font-weight: 400; }

  .brand { position: absolute; left: 52px; top: 1062px; width: 130px; text-align: center; }
  .brand-mark { display: block; width: 46px; height: 46px; margin: 0 auto 8px; border-radius: 50%; background: var(--amber); }
  .brand-name { font-family: "Open Sans", Arial, sans-serif; font-weight: 600; font-size: 16px; color: var(--grey); }

  .contact { position: absolute; left: 258px; top: 1070px; width: 340px; text-align: center; }
  .contact-call { display: flex; align-items: center; justify-content: center; gap: 12px; }
  .contact-icon { width: 40px; height: 40px; }
  .contact-phone { font-family: "Roboto Condensed", Arial, sans-serif; font-weight: 700; font-size: 31px; color: var(--ink); text-decoration: underline; text-underline-offset: 4px; }
  .contact-web { margin-top: 12px; font-size: 16px; font-weight: 600; color: var(--ink); letter-spacing: 0.5px; }

  .price-badge { position: absolute; left: 664px; top: 1024px; width: 162px; height: 162px; border-radius: 50%;
    background: radial-gradient(circle at 40% 35%, var(--pink) 0%, var(--pink-dark) 100%);
    color: var(--white); text-align: center; display: flex; flex-direction: column; justify-content: center; }
  .price-label { font-size: 20px; font-style: italic; font-weight: 600; letter-spacing: 1px; }
  .price-amount { font-family: "Montserrat", Arial, sans-serif; font-size: 44px; font-weight: 900; line-height: 1.05; }
  .price-period { font-size: 18px; font-style: italic; font-weight: 600; }
</style>
</head>
<body>
<div class="flyer">
  <div class="hero-backdrop" role="img" aria-label="Close-up photograph of banknotes in warm yellow tones"></div>

  <svg class="feature-band" viewBox="0 0 848 566" preserveAspectRatio="none" aria-hidden="true">
    <defs>
      <linearGradient id="bandFill" x1="0" y1="0" x2="0" y2="1">
        <stop offset="0" stop-color="#3b6c70"/>
        <stop offset="0.5" stop-color="#2a5258"/>
        <stop offset="1" stop-color="#1b3740"/>
      </linearGradient>
    </defs>
    <path d="M0 60 C 220 10, 520 10, 848 30 L848 566 L0 566 Z" fill="url(#bandFill)"/>
  </svg>

  <div class="team-photo" role="img" aria-label="Photograph of two smiling business people presenting a laptop with an online shop and a smartphone"></div>

  <h1 class="headline headline--navy headline-attract">ATTRACT MORE</h1>
  <p class="headline headline--red headline-customers">CUSTOMERS</p>
  <p class="headline headline--navy headline-make">MAKE MORE</p>
  <p class="headline headline--red headline-money">MONEY</p>

  <ul class="benefits">
    <li class="benefit"><svg class="tick" viewBox="0 0 30 26"><rect x="1" y="5" width="18" height="18" fill="#fff"/><path d="M4 14 L10 21 L27 2" fill="none" stroke="#e5262b" stroke-width="5" stroke-linecap="round" stroke-linejoin="round"/></svg>97% of people look online for businesses. You need a website</li>
    <li class="benefit"><svg class="tick" viewBox="0 0 30 26"><rect x="1" y="5" width="18" height="18" fill="#fff"/><path d="M4 14 L10 21 L27 2" fill="none" stroke="#e5262b" stroke-width="5" stroke-linecap="round" stroke-linejoin="round"/></svg>You're losing many customers by not having a website</li>
    <li class="benefit benefit--strong"><svg class="tick" viewBox="0 0 30 26"><rect x="1" y="5" width="18" height="18" fill="#fff"/><path d="M4 14 L10 21 L27 2" fill="none" stroke="#e5262b" stroke-width="5" stroke-linecap="round" stroke-linejoin="round"/></svg>Beat your competition with better visibility and credibility</li>
    <li class="benefit benefit--caps"><svg class="tick" viewBox="0 0 30 26"><rect x="1" y="5" width="18" height="18" fill="#fff"/><path d="M4 14 L10 21 L27 2" fill="none" stroke="#e5262b" stroke-width="5" stroke-linecap="round" stroke-linejoin="round"/></svg>Beautiful websites avalaible now</li>
    <li class="benefit"><svg class="tick" viewBox="0 0 30 26"><rect x="1" y="5" width="18" height="18" fill="#fff"/><path d="M4 14 L10 21 L27 2" fill="none" stroke="#e5262b" stroke-width="5" stroke-linecap="round" stroke-linejoin="round"/></svg>Smart, clean website designs ($3000 Value. No extra charge)</li>
    <li class="benefit"><svg class="tick" viewBox="0 0 30 26"><rect x="1" y="5" width="18" height="18" fill="#fff"/><path d="M4 14 L10 21 L27 2" fill="none" stroke="#e5262b" stroke-width="5" stroke-linecap="round" stroke-linejoin="round"/></svg>Limited to ONLY 4 WEBSITES per area. Don't miss out!</li>
    <li class="benefit"><svg class="tick" viewBox="0 0 30 26"><rect x="1" y="5" width="18" height="18" fill="#fff"/><path d="M4 14 L10 21 L27 2" fill="none" stroke="#e5262b" stroke-width="5" stroke-linecap="round" stroke-linejoin="round"/></svg>Social Media setup options</li>
  </ul>

  <p class="slogan slogan-stop"><span class="slogan-big">stop</span> wasting <span class="slogan-big">money</span></p>
  <p class="slogan slogan-sub">on mailers and print advertising.</p>

  <div class="brand">
    <span class="brand-mark"></span>
    <span class="brand-name">novasites</span>
  </div>

  <div class="contact">
    <div class="contact-call">
      <svg class="contact-icon" viewBox="0 0 40 40" aria-hidden="true"><circle cx="20" cy="20" r="19" fill="#1f7fd1"/><path d="M16 11 L26 20 L16 29" fill="none" stroke="#fff" stroke-width="4" stroke-linecap="round" stroke-linejoin="round"/></svg>
      <span class="contact-phone">CALL 1-800-555-0147</span>
    </div>
    <p class="contact-web">www.novasitesdemo.com</p>
  </div>

  <div class="price-badge">
    <span class="price-label">ONLY</span>
    <span class="price-amount">$99</span>
    <span class="price-period">PER MONTH</span>
  </div>
</div>
</body>
</html>
```